Rapidly growing regional logistics company looking for a modern clean website design.

We need a website for a 5 year old company based in New England.
We offer a complete logistics solution. With services dedicated to the changing economic environment. Services to our customers include, same day delivery, trucking and van service, warehouse & storage, pool distribution, and B2B installations.
We've implemented leading technology along the way, that provides visibility, accountability, up to the minute tracking, and project management.
Our goal to be known in the industry we service as an excellent provider of time-critical services and dependability.
Independently of the services we offer, our customers know that they can count on a true partner.

Target Market(s)

B2B, including printers, retail, manufacturers, wholesalers, electronics, any company that needs product delivered or warehoused

Industry/Entity Type

Logistics

Coding

Coded - Design and coding required

Number of Pages Required

5+ page

Font styles to use
Sans Serif

Colors
0255a3

Requirements
Must have
• Clean, modern design, limited clutter. Limited tabs, preferred everything on 1st screen roll down to see info

```html
<!DOCTYPE html>
<html lang="en">
<head>
<meta charset="utf-8">
<title>Harborline Logistics</title>
<link rel="stylesheet" href="https://fonts.googleapis.com/css2?family=Lato:wght@400;700&family=Open+Sans:wght@400;600&family=Roboto:wght@400;500&display=swap">
<style>
:root{
  --brand:#4769b3;
  --brand-dark:#3a5aa0;
  --ink:#2b2b2b;
  --muted:#555;
  --grey:#e4e4e4;
  --bar:#e9e9e9;
  --white:#fff;
  --dark-circle:#2c2c2c;
}
*{box-sizing:border-box;margin:0;padding:0}
html,body{width:1200px;height:2723px;overflow:hidden;background:var(--white)}
body{position:relative;font-family:"Open Sans",Arial,sans-serif;color:var(--ink)}
.abs{position:absolute}
.bands{position:absolute;left:0;top:0;z-index:0}
.layer{position:absolute;z-index:2}

/* header */
.brand-badge{left:81px;top:-3px;width:190px;height:190px;border-radius:50%;background:var(--white);z-index:5;display:flex;flex-direction:column;align-items:center;justify-content:center;gap:6px}
.brand-badge .dot{width:44px;height:44px;border-radius:50%;background:var(--brand)}
.brand-name{font-family:"Lato",sans-serif;font-weight:700;color:var(--brand);font-size:17px;text-align:center;line-height:1.1;letter-spacing:.5px}
.top-contact{right:98px;top:26px;display:flex;gap:30px;font-family:"Roboto",sans-serif;font-size:15px;color:var(--ink);z-index:3}
.top-contact span{display:flex;align-items:center;gap:10px}
.top-contact .ico{width:30px;height:30px;border-radius:50%;display:flex;align-items:center;justify-content:center}
.top-contact .phone .ico{background:var(--brand)}
.top-contact .mail .ico{background:var(--dark-circle)}
.top-contact .phone{color:var(--brand)}
.main-nav{right:98px;top:82px;display:flex;gap:27px;font-family:"Roboto",sans-serif;font-size:15px;font-weight:500;z-index:3}
.main-nav a{color:var(--ink);text-decoration:none}
.main-nav a.active{color:var(--brand)}

/* hero */
.hero-photo{left:0;top:123px;width:1200px;height:580px;background:linear-gradient(180deg,#4a5460 0%,#7b7b78 35%,#9a9690 60%,#6f6e6c 100%);z-index:0}
.hero-truck{left:60px;top:210px;width:520px;height:330px;background:linear-gradient(160deg,#c9cfd4 0%,#e0632d 55%,#9b3e1c 100%);opacity:.55;border-radius:6px;z-index:1}
.hero-copy{right:98px;top:222px;text-align:right;color:var(--white);z-index:2}
.hero-title{font-family:"Lato",sans-serif;font-weight:700;font-size:48px;letter-spacing:.5px}
.hero-sub{font-family:"Open Sans",sans-serif;font-weight:600;font-size:25px;margin-top:14px}
.hero-btn{display:inline-block;margin-top:36px;border:2px solid var(--white);padding:13px 16px;font-size:16px;font-weight:600;color:var(--white)}
.hero-dots{right:98px;top:465px;display:flex;gap:6px;z-index:2}
.hero-dots i{width:14px;height:14px;border-radius:50%;border:2px solid var(--white)}
.hero-dots i.on{background:#6a8fd8}

/* section headings */
.mark{width:40px;height:40px;border-radius:50%;background:var(--white);left:580px}
.sec-title{left:0;width:1200px;text-align:center;font-family:"Lato",sans-serif;font-weight:700;font-size:28px}
.rule{left:564px;width:72px;height:2px}
.light .sec-title{color:var(--white)}

/* about */
.about-text{left:140px;top:828px;width:920px;text-align:center;color:var(--white);font-size:13.5px;line-height:22px}
.about-btns{left:0;width:1200px;top:966px;display:flex;justify-content:center;gap:18px}
.btn{height:46px;width:102px;display:flex;align-items:center;justify-content:center;font-size:13.5px;font-weight:600;border-radius:2px}
.btn.solid{background:var(--white);color:var(--brand)}
.btn.ghost{border:2px solid var(--white);color:var(--white)}

/* services */
.service{width:460px;display:flex;gap:28px}
.service .art{width:94px;height:74px;flex:none;border-radius:6px}
.service h3{font-family:"Open Sans",sans-serif;font-weight:600;font-size:20px;color:var(--brand)}
.service p{font-size:13px;line-height:20px;color:#444;margin-top:10px;text-align:justify;width:336px}
.service .more{display:block;margin-top:14px;font-size:14px;font-weight:600;color:var(--brand)}

/* technology */
.tech{width:200px;text-align:center;color:var(--white)}
.tech .pin{width:150px;height:166px;margin:0 auto;display:block}
.tech h4{font-family:"Roboto",sans-serif;font-weight:500;font-size:18px;margin-top:8px;white-space:nowrap}
.tech p{font-size:12px;line-height:19px;margin:12px auto 0;width:170px}

/* footer */
.foot-brand{left:100px;top:2432px;width:170px;display:flex;flex-direction:column;align-items:center;gap:10px}
.foot-brand .dot{width:80px;height:80px;border-radius:50%;background:var(--brand)}
.foot-brand .brand-name{font-size:24px}
.foot-col h5{font-family:"Roboto",sans-serif;font-weight:500;font-size:17px;color:var(--brand)}
.foot-col h5::after{content:"";display:block;width:100px;height:2px;background:var(--brand);margin-top:10px}
.quick-links{list-style:none;margin-top:24px;font-family:"Roboto",sans-serif;font-size:15px}
.quick-links li{height:32px}
.quick-links li::before{content:"›";margin-right:6px}
.contact-item{display:flex;gap:18px;margin-top:14px}
.contact-item .ico{width:38px;height:38px;border-radius:50%;border:2px solid var(--brand);flex:none;display:flex;align-items:center;justify-content:center}
.contact-item b{font-family:"Roboto",sans-serif;font-weight:500;font-size:15px;display:block}
.contact-item span{font-size:12.5px;line-height:19px}
.field{position:absolute;border:1px solid #b9b9b9;font-size:11px;padding:8px 10px;color:#333}
.send{position:absolute;background:var(--brand);color:var(--white);font-family:"Roboto",sans-serif;font-weight:500;font-size:12px;display:flex;align-items:center;justify-content:center}

.bottom-bar{left:0;top:2659px;width:1200px;height:64px;background:var(--bar);z-index:2}
.copyright{left:100px;top:22px;font-size:14px}
.socials{left:900px;top:14px;display:flex;gap:10px}
.socials i{width:34px;height:34px;border-radius:50%;border:2px solid var(--ink)}
</style>
</head>
<body>

<svg class="bands" width="1200" height="2723" viewBox="0 0 1200 2723" aria-hidden="true">
  <rect x="0" y="1030" width="1200" height="690" fill="var(--grey)"/>
  <polygon points="0,680 600,626 1200,680 1200,1035 600,1093 0,1035" fill="var(--brand)"/>
  <polyline points="0,672 600,618 1200,672" fill="none" stroke="#fff" stroke-width="3"/>
  <polygon points="0,1706 600,1670 1200,1706 1200,2236 600,2291 0,2236" fill="var(--brand)"/>
</svg>

<!-- header -->
<div class="abs brand-badge">
  <div class="dot"></div>
  <div class="brand-name">HARBORLINE<br>LOGISTICS</div>
</div>
<div class="abs top-contact">
  <span class="phone"><span class="ico"><svg width="14" height="14" viewBox="0 0 24 24"><path fill="#fff" d="M6.6 10.8a15 15 0 006.6 6.6l2.2-2.2c.3-.3.7-.4 1-.2 1.1.4 2.3.6 3.6.6.6 0 1 .4 1 1V20c0 .6-.4 1-1 1C10.6 21 3 13.4 3 4c0-.6.4-1 1-1h3.5c.6 0 1 .4 1 1 0 1.3.2 2.5.6 3.6.1.3 0 .7-.2 1z"/></svg></span>180 555 0147</span>
  <span class="mail"><span class="ico"><svg width="14" height="14" viewBox="0 0 24 24"><path fill="none" stroke="#fff" stroke-width="2" d="M3 6h18v12H3zM3 6l9 7 9-7"/></svg></span>info@harborlinelogistics.com</span>
</div>
<nav class="abs main-nav">
  <a class="active">HOME</a><a>ABOUT US</a><a>OUR SERVICES</a><a>WAREHOUSING</a><a>BLOG</a><a>CONTACT US</a>
</nav>

<!-- hero -->
<div class="abs hero-photo" role="img" aria-label="Photo of orange freight trucks parked at a warehouse loading yard at dusk"></div>
<div class="abs hero-truck" role="img" aria-label="Orange articulated lorry in the foreground"></div>
<div class="abs hero-copy">
  <div class="hero-title">HARBORLINE LOGISTICS</div>
  <div class="hero-sub">Logistics Company from England</div>
  <div class="hero-btn">Read More</div>
</div>
<div class="abs hero-dots"><i></i><i class="on"></i><i></i><i></i><i></i></div>

<!-- about -->
<section class="light">
  <div class="layer mark" style="top:658px"></div>
  <h2 class="layer sec-title" style="top:724px">ABOUT HARBORLINE LOGISTICS</h2>
  <div class="layer rule" style="top:784px;background:var(--white)"></div>
  <p class="layer about-text">Our warehouse facility may prove to be one of the most valuable extensions of your company's operations. With a secure warehouse conveniently located in central New England to supplement your firm's storage and distribution needs. Pool Distribution is the distribution of product to numerous customers within a particular geographic region. This is a highly superior and cost-effective alternative to the higher cost of LTL shipments. In some instances, this could represent a 30%-70% savings vs. traditional LTL.</p>
  <div class="layer about-btns"><span class="btn solid">Read More</span><span class="btn ghost">Contact Us</span></div>
</section>

<!-- services -->
<section>
  <h2 class="layer sec-title" style="top:1144px;color:var(--brand)">OUR SERVICES</h2>
  <div class="layer rule" style="top:1200px;background:var(--brand)"></div>

  <div class="layer service" style="left:100px;top:1278px">
    <div class="art" role="img" aria-label="Illustration of a fast delivery van with a clock" style="background:#c6d2ea"></div>
    <div><h3>Trucking and van service</h3><p>Harborline Logistics offers a complete logistics solution. With services dedicated to the changing economic environment.</p><span class="more">Read More &gt;&gt;</span></div>
  </div>
  <div class="layer service" style="left:644px;top:1278px">
    <div class="art" role="img" aria-label="Illustration of a warehouse stacked with boxes" style="background:#e8b46a"></div>
    <div><h3>Warehouse &amp; storage</h3><p>Harborline Logistics offers a complete logistics solution. With services dedicated to the changing economic environment.</p><span class="more">Read More &gt;&gt;</span></div>
  </div>
  <div class="layer service" style="left:100px;top:1458px">
    <div class="art" role="img" aria-label="Illustration of a hand truck carrying a parcel" style="background:#efc865"></div>
    <div><h3>Pool distribution</h3><p>Harborline Logistics offers a complete logistics solution. With services dedicated to the changing economic environment.</p><span class="more">Read More &gt;&gt;</span></div>
  </div>
  <div class="layer service" style="left:644px;top:1458px">
    <div class="art" role="img" aria-label="Illustration of a clipboard checklist with a pencil" style="background:#f2cf7a"></div>
    <div><h3>B2B installations</h3><p>Harborline Logistics offers a complete logistics solution. With services dedicated to the changing economic environment.</p><span class="more">Read More &gt;&gt;</span></div>
  </div>
</section>

<!-- technology -->
<section class="light">
  <div class="layer mark" style="top:1686px"></div>
  <h2 class="layer sec-title" style="top:1763px">LEADING TECHNOLOGY</h2>
  <div class="layer rule" style="top:1821px;background:var(--white)"></div>

  <div class="layer tech" style="left:85px;top:1895px">
    <svg class="pin" viewBox="0 0 150 166"><path d="M75 4a69 69 0 0114 136.6L75 158l-14-17.4A69 69 0 0175 4z" fill="none" stroke="#fff" stroke-width="3"/><path d="M45 73q30-30 60 0q-30 30-60 0z" fill="#fff"/><circle cx="75" cy="73" r="9" fill="var(--brand)"/></svg>
    <h4>VISIBILITY</h4><p>Our warehouse facility may prove to be one of the most valuable extensions.</p>
  </div>
  <div class="layer tech" style="left:294px;top:1895px">
    <svg class="pin" viewBox="0 0 150 166"><path d="M75 4a69 69 0 0114 136.6L75 158l-14-17.4A69 69 0 0175 4z" fill="var(--dark-circle)" stroke="#fff" stroke-width="3"/><circle cx="70" cy="60" r="11" fill="none" stroke="#fff" stroke-width="3"/><path d="M50 94q0-18 20-18q12 0 16 6" fill="none" stroke="#fff" stroke-width="3"/><circle cx="88" cy="90" r="9" fill="#fff"/><path d="M84 90l3 3 5-6" fill="none" stroke="var(--dark-circle)" stroke-width="2"/></svg>
    <h4>ACCOUNTABILITY</h4><p>Our warehouse facility may prove to be one of the most valuable extensions.</p>
  </div>
  <div class="layer tech" style="left:503px;top:1895px">
    <svg class="pin" viewBox="0 0 150 166"><path d="M75 4a69 69 0 0114 136.6L75 158l-14-17.4A69 69 0 0175 4z" fill="none" stroke="#fff" stroke-width="3"/><circle cx="75" cy="73" r="22" fill="none" stroke="#fff" stroke-width="4"/><circle cx="75" cy="73" r="12" fill="none" stroke="#fff" stroke-width="3"/><circle cx="75" cy="73" r="4" fill="#fff"/></svg>
    <h4>MINUTE TRACKING</h4><p>Our warehouse facility may prove to be one of the most valuable extensions.</p>
  </div>
  <div class="layer tech" style="left:711px;top:1895px">
    <svg class="pin" viewBox="0 0 150 166"><path d="M75 4a69 69 0 0114 136.6L75 158l-14-17.4A69 69 0 0175 4z" fill="none" stroke="#fff" stroke-width="3"/><path d="M60 52h22l10 10v34H60z" fill="#fff"/><path d="M66 66h16M66 74h12" stroke="var(--brand)" stroke-width="3"/><circle cx="90" cy="90" r="9" fill="#fff" stroke="var(--brand)" stroke-width="3"/></svg>
    <h4>PROJECT MANAGEMENT</h4><p>Our warehouse facility may prove to be one of the most valuable extensions.</p>
  </div>
  <div class="layer tech" style="left:913px;top:1895px">
    <svg class="pin" viewBox="0 0 150 166"><path d="M75 4a69 69 0 0114 136.6L75 158l-14-17.4A69 69 0 0175 4z" fill="none" stroke="#fff" stroke-width="3"/><path d="M66 50a12 12 0 0112 12c0 9-12 22-12 22s-12-13-12-22a12 12 0 0112-12z" fill="#fff"/><circle cx="66" cy="62" r="4" fill="var(--brand)"/><rect x="70" y="76" width="22" height="16" fill="#fff"/><path d="M92 80h8l6 7v5H92z" fill="#fff"/><circle cx="78" cy="94" r="4" fill="#fff" stroke="var(--brand)" stroke-width="2"/><circle cx="99" cy="94" r="4" fill="#fff" stroke="var(--brand)" stroke-width="2"/></svg>
    <h4>SAME DAY DELIVERY</h4><p>Our warehouse facility may prove to be one of the most valuable extensions.</p>
  </div>
</section>

<!-- footer -->
<footer>
  <div class="layer foot-brand"><div class="dot"></div><div class="brand-name">HARBORLINE<br>LOGISTICS</div></div>

  <div class="layer foot-col" style="left:341px;top:2366px">
    <h5>QUICK LINKS</h5>
    <ul class="quick-links"><li>Home</li><li>Services</li><li>About Us</li><li>Warehouse</li><li>Blog</li><li>Contact Us</li></ul>
  </div>

  <div class="layer foot-col" style="left:535px;top:2366px;width:250px">
    <h5>CONTACT US</h5>
    <div class="contact-item" style="margin-top:22px"><span class="ico"><svg width="16" height="16" viewBox="0 0 24 24"><path d="M12 2a7 7 0 017 7c0 5-7 13-7 13S5 14 5 9a7 7 0 017-7z" fill="none" stroke="var(--brand)" stroke-width="2"/><circle cx="12" cy="9" r="2.5" fill="var(--brand)"/></svg></span><div><b>ADDRESS,</b><span>48 Mill Lane, Eastbrook,<br>UK, 5678</span></div></div>
    <div class="contact-item"><span class="ico"><svg width="14" height="16" viewBox="0 0 14 20"><rect x="1" y="1" width="12" height="18" rx="2" fill="none" stroke="var(--brand)" stroke-width="2"/><circle cx="7" cy="15" r="1.3" fill="var(--brand)"/></svg></span><div><b>PHONE:</b><span>180 555 0147</span></div></div>
    <div class="contact-item"><span class="ico"><svg width="16" height="14" viewBox="0 0 24 18"><path d="M2 2h20v14H2zM2 2l10 8 10-8" fill="none" stroke="var(--brand)" stroke-width="2"/></svg></span><div><b>Mail:</b><span>info@harborlinelogistics.com</span></div></div>
  </div>

  <div class="layer foot-col" style="left:813px;top:2366px;width:290px;height:240px">
    <h5>CONTACT FORM</h5>
    <div class="field" style="left:0;top:64px;width:136px;height:34px">Name</div>
    <div class="field" style="left:149px;top:64px;width:136px;height:34px">Phone</div>
    <div class="field" style="left:0;top:106px;width:285px;height:64px">Message</div>
    <div class="send" style="left:0;top:188px;width:118px;height:36px">SEND MESSAGE</div>
  </div>

  <div class="abs bottom-bar">
    <div class="abs copyright">Copyright © 2017 Harborline Logistics. All Rights Reserved.</div>
    <div class="abs socials"><i></i><i></i><i></i><i></i><i></i></div>
  </div>
</footer>

</body>
</html>
```